Holistic Psychology clinic flyer-

We need a 3 fold flyer that is both professional and zen looking with holistic elements- bilingual on both sides.
I am looking for a design that conveys the sense of confidence, yet relaxing to the eye and makes people want to pick it up and read it!
We are all about balance (yin, yang) and bringing equilibrium to a person in their quest to get better.

Target Market(s)

families adults, teens children experiencing mental health issues

Industry/Entity Type

Psychologist

Font styles to use
Serif

Colors
fbf289
cee9f5
0455a3

Requirements
Must have
• my logo (spiral) ; French one side; English on the other. Text is provided; Some color but clean, zen elements
• Easy to read text
Nice to have
• nature elements, bamboo? trees etc. sunrise or sunset?
• The sunset back ground provided in the picture is not necessary
• families?
Should not have
• too many distracting elements; not too many colors. colors must be subtle and must flow together

```html
<!DOCTYPE html>
<html lang="en">
<head>
<meta charset="utf-8">
<title>Sérénova – Trifold Outside</title>
<link href="https://fonts.googleapis.com/css2?family=Lato:wght@400;700;900&family=Montserrat:wght@600;700;800&display=swap" rel="stylesheet">
<style>
  :root{
    --navy:#0455a3;
    --navy-deep:#063f7c;
    --sky:#cee9f5;
    --sun:#fbf289;
    --gold:#f6d23c;
    --ink:#3b4250;
    --paper:#ffffff;
    --stage:#eef1f4;
  }
  *{box-sizing:border-box;margin:0;padding:0}
  html,body{width:831px;height:1200px;overflow:hidden}
  body{background:var(--stage);font-family:"Lato",Arial,sans-serif;color:var(--ink);position:relative}

  .brochure{position:absolute;left:15px;top:290px;width:801px;height:620px;background:var(--paper);
    display:grid;grid-template-columns:267px 267px 267px;box-shadow:0 6px 24px rgba(0,0,0,.15)}
  .panel{position:relative;height:620px;overflow:hidden}

  /* services panel */
  .services{padding:16px 14px}
  .services__box{background:var(--navy);border-radius:10px;height:100%;padding:20px 16px;color:#fff}
  .services__title{font-family:"Montserrat",sans-serif;font-weight:800;font-size:18px;color:var(--sun);margin-bottom:14px;text-align:center}
  .service{margin-bottom:13px}
  .service__name{font-family:"Montserrat",sans-serif;font-weight:700;font-size:10px;color:var(--sun);margin-bottom:4px}
  .service__text{font-size:8px;line-height:1.45;color:#e9f3fb}

  /* welcome panel */
  .welcome{padding:26px 20px 18px;display:flex;flex-direction:column}
  .welcome__pre{font-family:"Montserrat",sans-serif;font-weight:600;font-size:16px;color:var(--navy)}
  .welcome__name{font-family:"Montserrat",sans-serif;font-weight:800;font-size:27px;color:var(--navy);line-height:1.1;margin-bottom:14px}
  .welcome p{font-size:8.4px;line-height:1.55;margin-bottom:10px}
  .welcome .tagline{font-weight:700;color:var(--navy);font-size:9px}
  .contact{margin-top:auto;text-align:center}
  .contact__title{font-family:"Montserrat",sans-serif;font-weight:700;font-size:13px;color:var(--navy);margin-bottom:8px}
  .contact__social{display:flex;justify-content:center;gap:7px;margin-bottom:9px}
  .contact__social span{width:16px;height:16px;border-radius:50%;background:var(--navy);display:block}
  .contact__line{font-size:8.2px;line-height:1.5}
  .contact__phone{display:flex;align-items:center;justify-content:center;gap:5px;font-weight:700;color:var(--navy);font-size:9px;margin-top:4px}

  /* cover panel */
  .cover__art{position:absolute;inset:0}
  .brand{position:absolute;top:18px;right:22px;display:flex;align-items:center;gap:6px;z-index:2}
  .brand__dot{width:16px;height:16px;border-radius:50%;background:var(--gold)}
  .brand__name{font-family:"Montserrat",sans-serif;font-weight:700;font-size:22px;color:var(--navy)}
  .cover__copy{position:absolute;left:62px;right:16px;top:372px;text-align:right;color:#fff;z-index:2}
  .cover__title{font-family:"Montserrat",sans-serif;font-weight:700;font-size:17px;line-height:1.2;margin-bottom:12px}
  .cover__audience{font-family:"Montserrat",sans-serif;font-weight:800;font-size:11px;color:var(--sun);letter-spacing:.3px}
  .cover__web{position:absolute;bottom:16px;right:18px;font-size:8.5px;color:#fff;z-index:2}
</style>
</head>
<body>
<main class="brochure">

  <section class="panel services">
    <div class="services__box">
      <h2 class="services__title">Our Professional Services</h2>
      <div class="service"><h3 class="service__name">Clinical Psychology</h3>
        <p class="service__text">Assessment and treatment of anxiety, mood and behavioural difficulties, offered with care to children, teens, adults and couples.</p></div>
      <div class="service"><h3 class="service__name">Integrative Psychotherapy</h3>
        <p class="service__text">We blend several therapeutic approaches to suit your needs, bringing body, mind and emotions back into balance.</p></div>
      <div class="service"><h3 class="service__name">Life Coaching</h3>
        <p class="service__text">Practical guidance to set clear goals, build confidence and move forward with calm through each stage of life.</p></div>
      <div class="service"><h3 class="service__name">Sports Psychology</h3>
        <p class="service__text">Support for athletes who want to sharpen focus, manage pressure and perform at their best with a steady mind.</p></div>
      <div class="service"><h3 class="service__name">Psycho-Educational Assessments</h3>
        <p class="service__text">Thorough evaluations of learning, attention and development, with clear recommendations for families and schools.</p></div>
      <div class="service"><h3 class="service__name">Mindfulness Meditation Classes</h3>
        <p class="service__text">Small group classes teaching simple breathing and awareness practices that bring quiet and equilibrium to daily life.</p></div>
    </div>
  </section>

  <section class="panel welcome">
    <h2 class="welcome__pre">Welcome to</h2>
    <h1 class="welcome__name">Sérénova</h1>
    <p>Welcome to a space where you are heard. Our team of psychologists and educational professionals offers warm, confidential support, combining proven methods with an integrative view of the whole person so that each step toward wellbeing feels steady and clear.</p>
    <p class="tagline">Care you need. Help you trust. Results you feel.</p>
    <p>Our founder brings many years of clinical experience with children, teens, adults and couples. Every plan is built around your goals, your pace and your values, with kindness and respect.</p>
    <p>We are happy to answer your questions and to find a time that works for you and your family.</p>
    <div class="contact">
      <h3 class="contact__title">Contact us today</h3>
      <div class="contact__social"><span></span><span></span><span></span><span></span><span></span></div>
      <p class="contact__line">2100 Rue des Érables, Montréal</p>
      <p class="contact__line">QC H0H 0H0</p>
      <p class="contact__phone">
        <svg width="10" height="10" viewBox="0 0 24 24"><path fill="#0455a3" d="M6.6 10.8a15 15 0 0 0 6.6 6.6l2.2-2.2a1 1 0 0 1 1-.25 11.4 11.4 0 0 0 3.6.57 1 1 0 0 1 1 1V20a1 1 0 0 1-1 1A17 17 0 0 1 3 4a1 1 0 0 1 1-1h3.5a1 1 0 0 1 1 1c0 1.25.2 2.45.57 3.57a1 1 0 0 1-.25 1z"/></svg>
        514-555-0142
      </p>
    </div>
  </section>

  <section class="panel cover">
    <svg class="cover__art" width="267" height="620" viewBox="0 0 267 620">
      <defs>
        <radialGradient id="sunset" cx="50%" cy="60%" r="60%">
          <stop offset="0" stop-color="#fde7a0"/>
          <stop offset=".45" stop-color="#f5a23a"/>
          <stop offset="1" stop-color="#8a3d12"/>
        </radialGradient>
      </defs>
      <path d="M0 250 Q60 360 267 330 L267 620 L0 620 Z" fill="#0455a3"/>
      <path d="M0 300 Q80 390 267 360" fill="none" stroke="#cee9f5" stroke-width="3"/>
      <circle cx="150" cy="215" r="150" fill="#ffffff"/>
      <circle cx="150" cy="215" r="140" fill="url(#sunset)" role="img" aria-label="Photo of a person leaping joyfully in silhouette against a sunset sky"/>
    </svg>
    <div class="brand"><span class="brand__dot"></span><span class="brand__name">Sérénova</span></div>
    <div class="cover__copy">
      <h2 class="cover__title">Clinique Sérénova Psychologists and Educational Professionals with and Integrative Approach</h2>
      <p class="cover__audience">CHILDREN. TEENS. ADULTS. COUPLES.</p>
    </div>
    <p class="cover__web">www.serenova-example.com</p>
  </section>

</main>
</body>
</html>
```